Business cards for law firm with global theme

I'd like business cards with contact info for two offices. They should include the colors and font of the new logo design, which is a stylized globe with an "F" in it. The feel should be very modern and professional.

```html
<!DOCTYPE html>
<html lang="en">
<head>
<meta charset="utf-8">
<title>Meridane Law — Business Cards</title>
<link href="https://fonts.googleapis.com/css2?family=Montserrat:wght@400;500;700&display=swap" rel="stylesheet">
<style>
  :root{
    --backdrop:#2a2a2a;
    --blue-deep:#1b6aa3;
    --blue-mid:#2e8fcb;
    --blue-light:#4aa9dd;
    --cyan:#36ade4;
    --navy:#173f6d;
    --ink:#2b2b2b;
    --white:#ffffff;
  }
  *{margin:0;padding:0;box-sizing:border-box}
  html,body{width:1200px;height:1186px;overflow:hidden}
  body{background:var(--backdrop);font-family:'Montserrat',sans-serif;position:relative}
  .card{position:absolute;left:160px;width:880px;height:500px;border-radius:28px;overflow:hidden}
  .card-front{top:60px;background:linear-gradient(120deg,var(--blue-deep) 0%,var(--blue-mid) 55%,var(--blue-light) 100%)}
  .card-front .glow{position:absolute;inset:0;background:radial-gradient(ellipse at 75% 20%,rgba(255,255,255,.18),rgba(255,255,255,0) 60%)}
  .front-brand{position:absolute;left:0;right:0;top:150px;display:flex;flex-direction:column;align-items:center}
  .front-brand .mark{width:110px;height:110px;border-radius:50%;background:var(--white);margin-bottom:22px}
  .front-brand .name{font-weight:700;font-size:64px;letter-spacing:2px;color:var(--white);line-height:1}
  .front-brand .rule{width:470px;height:2px;background:var(--white);margin-top:18px;opacity:.9}
  .card-back{top:626px;background:var(--white)}
  .card-back svg.bands{position:absolute;inset:0}
  .back-brand{position:absolute;left:60px;top:130px;display:flex;align-items:center;gap:22px}
  .back-brand .mark{width:86px;height:86px;border-radius:50%;background:var(--cyan)}
  .back-brand .name{font-weight:700;font-size:40px;letter-spacing:1px;color:var(--navy);line-height:1}
  .person{position:absolute;left:70px;top:296px;color:var(--white)}
  .person .full-name{font-weight:700;font-size:26px;line-height:1}
  .person .role{font-weight:400;font-size:15px;margin-top:6px}
  .contacts{list-style:none;margin-top:12px}
  .contacts li{display:flex;align-items:center;gap:12px;font-size:16px;line-height:24px}
  .contacts svg{width:14px;height:14px;flex:none}
  .address{position:absolute;left:70px;top:450px;font-size:16px;line-height:22px;color:var(--ink)}
</style>
</head>
<body>
  <section class="card card-front" aria-label="Card front">
    <div class="glow"></div>
    <div class="front-brand">
      <div class="mark"></div>
      <div class="name">MERIDANE LAW</div>
      <div class="rule"></div>
    </div>
  </section>

  <section class="card card-back" aria-label="Card back">
    <svg class="bands" viewBox="0 0 880 500" preserveAspectRatio="none">
      <polygon points="640,162 880,114 880,0 640,20" fill="var(--navy)"/>
      <polygon points="0,290 880,114 880,372 0,460" fill="var(--cyan)"/>
    </svg>
    <div class="back-brand">
      <div class="mark"></div>
      <div class="name">MERIDANE LAW</div>
    </div>
    <div class="person">
      <div class="full-name">Daniel Carver</div>
      <div class="role">CEO &amp; Founder</div>
      <ul class="contacts">
        <li><svg viewBox="0 0 16 16"><path fill="#fff" d="M3 1h3l1.5 4-2 1.2a9 9 0 0 0 4.3 4.3L11 8.5l4 1.5v3a2 2 0 0 1-2 2A12 12 0 0 1 1 3a2 2 0 0 1 2-2z"/></svg>(555) 014-2290</li>
        <li><svg viewBox="0 0 16 16"><rect x="1" y="3" width="14" height="10" rx="1" fill="#fff"/><path d="M1 4l7 5 7-5" stroke="var(--cyan)" stroke-width="1.4" fill="none"/></svg>info@meridanelaw.com</li>
        <li><svg viewBox="0 0 16 16"><circle cx="8" cy="8" r="7" fill="#fff"/><path d="M1 8h14M8 1c-3 3-3 11 0 14M8 1c3 3 3 11 0 14" stroke="var(--cyan)" stroke-width="1" fill="none"/></svg>www.meridanelaw.com</li>
      </ul>
    </div>
    <div class="address">420 Harbor Avenue, Suite 900<br>Bayview, CA 90000</div>
  </section>
</body>
</html>
```